User profile management app in Bootstrap & AngularJS

We have a single page web app with front end built on AngularJS and Bootstrap. There is a navbar on top and about 10 different views (user profile view, user profile edit, update-able list of items, help section, ...). At this point the app has functionality but no graphics or thought-out layout.

Need a designer to take the existing HTML, CSS (or even JS) files and modify and expand them to make the app look good. Find the existing HTML and JS files for the client attached. You'll need to download angular, bootstrap and ng-map libraries separately.

You can experience the code live at https://design.kelvo.net/kelvoportal.html

The templates provided are text-only but the result should contain a few icons for better visual experience. Some suggested areas for images include device types (email, cell phone, pager, landline phone, ...), status indicators (true/false, on/off, enabled/disabled, ...), navigation (expand/collapse, previous page/next page, ...), file download, CRUD management (add, edit, delete), help popups, etc

The resulting design and code should be mobile-friendly and handicap-accessible (Section 508 compliant).

Font desired: Univers family but not required, otherwise Arial
Only use color from the list provided in the attached file. Colors should not indicate a specific meaning and the whole design should be primarily blue (RGB R0 G103 B198) and white themed.

Allow for banner somewhere on top of page - about 530 x 100 pixels. Allow for a footer with an image on the left and 2-3 sentences of text (copyright, disclaimer, etc).
Updates

Target Market(s)

general public, design for simplicity and ease of use

Industry/Entity Type

Cell Phone

Coding

Coded - Design and coding required

Number of Pages Required

5+ page

Font styles to use
Sans Serif
Other font styles liked:
• Univers family preferred not required otw Arial

Requirements
Must have
• Use blue (RGB R0 G103 B198) and white theme. Must be mobile friendly and handicap-enabled.
• Icons: Use the three stroke weights; light, medium, bold.
• Icons can be designed as outlines or solid silhouettes in two-dimensional form. Icons must be recognizable to a majority of the intended audience. Avoid fine lines and overly complex imagery.

```html
<!DOCTYPE html>
<html lang="en">
<head>
<meta charset="utf-8">
<title>Kelvo Portal – Home</title>
<link href="https://fonts.googleapis.com/css2?family=Open+Sans:wght@400;600;700&display=swap" rel="stylesheet">
<style>
:root{
  --blue:#0067c6;
  --blue-dark:#00509a;
  --blue-soft:#e8f1fb;
  --blue-line:#c9dcf0;
  --ink:#333333;
  --ink-soft:#4a5a6a;
  --muted:#8fa3b8;
  --line:#d5e2ef;
  --canvas:#f4f8fc;
  --panel-top:#f5f9fd;
  --panel-bottom:#e3eef9;
  --thead-top:#ffffff;
  --thead-bottom:#edf3fa;
  --row-alt:#f7fafd;
  --footer-text:#d6e6f6;
  --white:#ffffff;
}
*{box-sizing:border-box;margin:0;padding:0}
html,body{width:1200px;height:2840px;overflow:hidden;background:var(--canvas)}
body{font-family:"Open Sans",Arial,sans-serif;color:var(--ink)}
.page{width:480px;height:1136px;transform:scale(2.5);transform-origin:0 0;position:relative;background:var(--canvas)}

.topbar{height:50px;background:var(--blue);display:flex;align-items:center;justify-content:space-between;padding:0 11px}
.brand{color:var(--white);font-weight:700;font-size:20px;letter-spacing:.3px}
.menu-toggle{width:40px;height:28px;background:var(--blue-dark);border-radius:4px;display:flex;flex-direction:column;justify-content:center;align-items:center;gap:4px;border:1px solid rgba(255,255,255,.35)}
.menu-toggle span{display:block;width:18px;height:2px;background:var(--white);border-radius:1px}

.main-nav{background:var(--white);height:217px;border-bottom:1px solid var(--line);display:grid;grid-template-columns:158px 158px 164px;grid-auto-rows:70px}
.nav-item{display:flex;flex-direction:column;align-items:center;justify-content:center;gap:5px;font-size:12px;font-weight:600;color:var(--muted);text-decoration:none;position:relative}
.nav-item svg{width:18px;height:18px;fill:currentColor}
.nav-item.active{color:var(--blue)}
.nav-item.active::after{content:"";position:absolute;left:0;right:0;bottom:-3px;height:3px;background:var(--blue)}

.content{padding:33px 20px 62px;height:765px}
.panel{background:var(--white);border:1px solid var(--line);border-radius:3px;overflow:hidden;margin-bottom:27px}
.panel-head{height:42px;background:linear-gradient(var(--panel-top),var(--panel-bottom));border-bottom:1px solid var(--line);display:flex;align-items:center;padding:0 12px;gap:10px;font-size:15px;color:var(--ink)}
.panel-head svg{width:16px;height:16px;fill:var(--blue)}
.panel-head .title{flex:1}
.send-btn{background:var(--blue);color:var(--white);font:400 14px "Open Sans",Arial,sans-serif;border:none;border-radius:3px;width:60px;height:28px;margin-right:-6px}

.data-table{border-collapse:collapse;width:100%;font-size:13px;table-layout:fixed}
.data-table th{background:linear-gradient(var(--thead-top),var(--thead-bottom));text-transform:uppercase;font-size:9.5px;font-weight:600;color:var(--ink-soft);text-align:left;padding:0 8px;height:34px;border-right:1px solid var(--line);border-bottom:1px solid var(--line);line-height:1.9}
.data-table td{padding:0 8px;height:35px;border-right:1px solid var(--line);border-bottom:1px solid var(--line)}
.data-table th:last-child,.data-table td:last-child{border-right:none}
.data-table tbody tr:nth-child(odd){background:var(--row-alt)}
.data-table tbody tr:last-child td{border-bottom:none}
.profile-table th,.profile-table td{padding:0 6px}
.profile-table th{height:52px}
.profile-table td{height:52px;line-height:1.4}

.site-footer{position:absolute;left:0;right:0;bottom:0;height:105px;background:var(--blue);display:flex;align-items:center;justify-content:center;font-size:11.5px;color:var(--footer-text)}
</style>
</head>
<body>
<div class="page">
  <header class="topbar">
    <span class="brand">BRAND</span>
    <div class="menu-toggle" role="button" aria-label="Open menu"><span></span><span></span><span></span></div>
  </header>

  <nav class="main-nav" aria-label="Main">
    <a class="nav-item active" href="#home"><svg viewBox="0 0 20 20"><path d="M10 2 1 10h3v8h5v-5h2v5h5v-8h3z"/></svg>Home</a>
    <a class="nav-item" href="#devices"><svg viewBox="0 0 20 20"><path d="M1 3h18v14H1zm2 2v10h14V5zm2 2h10v1.5H5zm0 3h10v1.5H5zm0 3h10v1.5H5z"/></svg>Devices</a>
    <a class="nav-item" href="#locations"><svg viewBox="0 0 20 20"><path d="M10 1a6 6 0 0 0-6 6c0 5 6 12 6 12s6-7 6-12a6 6 0 0 0-6-6zm0 8.5A2.5 2.5 0 1 1 10 4.5a2.5 2.5 0 0 1 0 5z"/></svg>Locations</a>
    <a class="nav-item" href="#profile"><svg viewBox="0 0 20 20"><circle cx="10" cy="6" r="4.5"/><path d="M2 19c0-5 3.5-7 8-7s8 2 8 7z"/></svg>Profile</a>
    <a class="nav-item" href="#subscriptions"><svg viewBox="0 0 20 20"><circle cx="4" cy="16" r="2.3"/><path d="M2 8v3a7 7 0 0 1 7 7h3A10 10 0 0 0 2 8zm0-6v3a13 13 0 0 1 13 13h3A16 16 0 0 0 2 2z"/></svg>Subscriptions</a>
    <a class="nav-item" href="#alerts"><svg viewBox="0 0 20 20"><path d="M10 1a9 9 0 1 0 0 18 9 9 0 0 0 0-18zm-1.3 4h2.6l-.4 6.5H9.1zM10 13a1.5 1.5 0 1 1 0 3 1.5 1.5 0 0 1 0-3z"/></svg>Alert Log</a>
    <a class="nav-item" href="#help"><svg viewBox="0 0 20 20"><path d="M10 1a9 9 0 1 0 0 18 9 9 0 0 0 0-18zm1 14H9v-2h2zm1.6-5.6-.9.7c-.5.4-.7.8-.7 1.4H9c0-1.1.4-1.7 1.2-2.3l1-.8a1.4 1.4 0 0 0-1.1-2.4c-.8 0-1.4.6-1.5 1.4H7a3.2 3.2 0 0 1 6.3-.3c.1.9-.2 1.7-.7 2.3z"/></svg>Help</a>
  </nav>

  <main class="content">
    <section class="panel">
      <div class="panel-head"><svg viewBox="0 0 20 20"><circle cx="10" cy="6" r="4.5"/><path d="M2 19c0-5 3.5-7 8-7s8 2 8 7z"/></svg><span class="title">User Profile</span></div>
      <table class="data-table profile-table">
        <colgroup><col style="width:44px"><col style="width:48px"><col style="width:116px"><col style="width:60px"><col style="width:78px"><col></colgroup>
        <thead><tr><th>First name</th><th>Last name</th><th>Email address</th><th>City</th><th>State</th><th>Languages</th></tr></thead>
        <tbody><tr><td>John</td><td>Smith</td><td>admin@email.com</td><td>Gotham</td><td>AMERICAN SAMOA</td><td>French<br>Spanish</td></tr></tbody>
      </table>
    </section>

    <section class="panel">
      <div class="panel-head"><svg viewBox="0 0 20 20"><circle cx="10" cy="6" r="3.3"/><path d="M4.5 17c0-3.8 2.4-5.6 5.5-5.6s5.5 1.8 5.5 5.6z"/><circle cx="4" cy="7.5" r="2.3"/><circle cx="16" cy="7.5" r="2.3"/><path d="M0 15c0-2.8 1.6-4 3.8-4 .6 0 1 .1 1.5.3A7 7 0 0 0 3.5 15zm20 0c0-2.8-1.6-4-3.8-4-.6 0-1 .1-1.5.3a7 7 0 0 1 1.8 3.7z"/></svg><span class="title">Groups</span></div>
      <table class="data-table">
        <colgroup><col style="width:133px"><col style="width:142px"><col></colgroup>
        <thead><tr><th>Group name</th><th>Category</th><th>Type</th></tr></thead>
        <tbody>
          <tr><td>Group One</td><td>Category Top</td><td>Group Type Top</td></tr>
          <tr><td>Group Two</td><td>Category Top</td><td>Group Type Top</td></tr>
          <tr><td>Group Three</td><td>Category Top</td><td>Group Type Top</td></tr>
          <tr><td>Group Four</td><td>Category Top</td><td>Group Type Top</td></tr>
          <tr><td>Group Five</td><td>Category Top</td><td>Group Type Top</td></tr>
        </tbody>
      </table>
    </section>

    <section class="panel">
      <div class="panel-head"><svg viewBox="0 0 20 20"><path d="M1 3h18v14H1zm2 2v10h14V5zm2 2h10v1.5H5zm0 3h10v1.5H5zm0 3h10v1.5H5z"/></svg><span class="title">Devices</span><button class="send-btn" type="button">Send</button></div>
      <table class="data-table">
        <colgroup><col style="width:206px"><col style="width:148px"><col></colgroup>
        <thead><tr><th>Device identifier</th><th>Delivery channel</th><th>Status</th></tr></thead>
        <tbody>
          <tr><td>johnsmith@nolvex.com</td><td>E-mail account</td><td>Enabled</td></tr>
          <tr><td>(123)456-7890</td><td>telvo</td><td>Enabled</td></tr>
          <tr><td>johnsmith@nolvex.com2</td><td>E-mail account</td><td>Alias</td></tr>
          <tr><td>frghfgh@ghfgh.com</td><td>E-mail account</td><td>Enabled</td></tr>
        </tbody>
      </table>
    </section>
  </main>

  <footer class="site-footer">© 2015 Brand. All right reserved.</footer>
</div>
</body>
</html>
```